Mobile Fitness snd Therapy Business Card Design

I need a business card designed for my mobile fitness and therapy business.

Please view the images that I have uploaded. I like the simplicity of the design that I have attached. I adapted it with my information

Target Market(s)

Those seeking personal training, injury rehabilitation or massage therapy.

Industry/Entity Type

Business

Contact Information for Business Card

Derek Holloway - MSc, CAT(C), RMT, CSCS, Pn2
e-mail: derek@bravuumfit.example
website: www.bravuumfit.example
instagram: @derek_holloway

Font styles to use
Sans Serif

Colors
3176b5
0355a3

Requirements
Must have
• "Contact us to receive a FREE assessment"
• Services offered:
• Personal Training
• Golf Fitness
• Injury Rehab
• Massage Therapy
• Yoga
Nice to have
• Consistent colours with brand
• - Dark Blue: #232837
• - Blue: #5096f0
• Consistent look/feel with the website: www.bravuumfit.example

```html
<!DOCTYPE html>
<html lang="en">
<head>
<meta charset="utf-8">
<title>Bravuum Business Card</title>
<link rel="stylesheet" href="https://fonts.googleapis.com/css2?family=Roboto:wght@400;500;700;900&display=swap">
<style>
  :root {
    --bg: #e4e4e4;
    --navy: #232837;
    --navy-light: #343a4b;
    --blue: #3a9ae6;
    --blue-deep: #0355a3;
    --line-blue: #5aaee8;
    --white: #ffffff;
    --text-dark: #1f2433;
  }
  * { box-sizing: border-box; margin: 0; padding: 0; }
  html, body { width: 1200px; height: 852px; overflow: hidden; }
  body {
    background: var(--bg);
    font-family: "Roboto", Arial, sans-serif;
    position: relative;
  }
  .card {
    position: absolute;
    top: 276px;
    width: 520px;
    height: 300px;
    border-radius: 22px;
    overflow: hidden;
    box-shadow: 0 6px 18px rgba(0,0,0,0.18);
  }

  /* Back */
  .card-back {
    left: 60px;
    background: linear-gradient(160deg, var(--navy-light), var(--navy) 65%);
  }
  .back-brand {
    position: absolute;
    top: 88px; left: 0; width: 100%;
    text-align: center;
    font-weight: 900;
    font-size: 46px;
    letter-spacing: 6px;
    color: var(--blue);
  }
  .services {
    position: absolute;
    right: 30px; bottom: 30px;
    text-align: right;
    color: var(--white);
    font-size: 13px;
    line-height: 19px;
  }
  .services .sep {
    display: inline-block;
    width: 6px; height: 6px;
    background: var(--blue);
    margin: 0 6px 2px;
  }

  /* Front */
  .card-front {
    left: 620px;
    background: var(--white);
  }
  .brand {
    position: absolute;
    top: 34px; right: 34px;
    text-align: right;
  }
  .brand-name {
    font-weight: 900;
    font-size: 40px;
    letter-spacing: 4px;
    color: var(--text-dark);
    line-height: 1;
  }
  .brand-tagline {
    margin-top: 6px;
    font-weight: 700;
    font-size: 11.5px;
    letter-spacing: 2.4px;
    color: var(--text-dark);
  }
  .divider {
    position: absolute;
    top: 118px; right: 34px;
    width: 270px; height: 1.5px;
    background: var(--line-blue);
  }
  .person {
    position: absolute;
    left: 30px; top: 136px;
  }
  .person-name {
    font-weight: 700;
    font-size: 24px;
    color: var(--text-dark);
    letter-spacing: 0.3px;
  }
  .credentials {
    font-size: 13px;
    color: var(--blue);
    margin-top: 2px;
  }
  .contacts {
    list-style: none;
    margin-top: 12px;
    font-size: 14px;
    color: var(--text-dark);
  }
  .contacts li {
    display: flex;
    align-items: center;
    gap: 8px;
    line-height: 20px;
  }
  .contacts svg { width: 13px; height: 13px; flex: none; }
  .contacts .hl { color: var(--blue); }
  .social {
    position: absolute;
    right: 34px; bottom: 66px;
    display: flex; align-items: center; gap: 7px;
    font-size: 13px;
    color: var(--text-dark);
  }
  .social .dot {
    width: 11px; height: 11px;
    border: 1.6px solid var(--blue);
    border-radius: 50%;
  }
  .cta-band {
    position: absolute;
    right: 0; bottom: 8px;
    width: 400px; height: 42px;
    background: var(--navy);
    border-top-left-radius: 22px;
    display: flex; align-items: center; justify-content: center;
    color: var(--white);
    font-size: 14.5px;
  }
  .cta-band .free { color: var(--blue); }
  .accent-strip {
    position: absolute;
    left: 0; right: 0; bottom: 0;
    height: 8px;
    background: var(--blue);
  }
</style>
</head>
<body>

<section class="card card-back" aria-label="Card back">
  <div class="back-brand">BRAVUUM</div>
  <div class="services">
    Personal Training<span class="sep"></span>Nutrition Coaching<span class="sep"></span>Golf Fitness<br>
    Injury Rehabilitation<span class="sep"></span>Massage Therapy<span class="sep"></span>Yoga
  </div>
</section>

<section class="card card-front" aria-label="Card front">
  <div class="brand">
    <div class="brand-name">BRAVUUM</div>
    <div class="brand-tagline">NUTRITION - FITNESS - HEALTH</div>
  </div>
  <div class="divider"></div>

  <div class="person">
    <div class="person-name">DEREK HOLLOWAY</div>
    <div class="credentials">MSc, CAT(C), RMT, CSCS, Pn2</div>
    <ul class="contacts">
      <li>
        <svg viewBox="0 0 16 16" fill="none" stroke="#3a9ae6" stroke-width="1.6"><circle cx="8" cy="8" r="7"/><path d="M5.5 4.5l1.5 1.5-1 1a5 5 0 003 3l1-1 1.5 1.5-1 1c-3 0-6-3-6-6z" fill="#3a9ae6" stroke="none"/></svg>
        250-555-0174
      </li>
      <li>
        <svg viewBox="0 0 16 16" fill="none" stroke="#3a9ae6" stroke-width="1.6"><rect x="1" y="3" width="14" height="10"/><path d="M1 3l7 6 7-6"/></svg>
        derek@bravuumfit.example
      </li>
      <li>
        <svg viewBox="0 0 16 16" fill="none" stroke="#3a9ae6" stroke-width="1.4"><circle cx="8" cy="8" r="7"/><ellipse cx="8" cy="8" rx="3" ry="7"/><path d="M1 8h14"/></svg>
        <span>www.<span class="hl">bravuumfit</span>.example</span>
      </li>
    </ul>
  </div>

  <div class="social"><span class="dot"></span>@derek_holloway</div>

  <div class="cta-band">Contact us to receive a&nbsp;<span class="free">FREE</span>&nbsp;assessment</div>
  <div class="accent-strip"></div>
</section>

</body>
</html>
```